Female Pest Controller needs awesome business cards

I need a logo design for a Pest Control service - something that appeals to 'nature' & safe, with the use of the colour green. I am also female
New Business Name is 'Bug Begone Bay'
appeals to women

Target Market(s)

Domestic Households & Local Businesses

Industry/Entity Type

Pest Control

Contact Information for Business Card

Corinne Waldrake
0428316952
ABN 47 618 259 304
PMT7314958207
Spiders Cockroaches, Ants, Silverfish, Fleas, Rodents

Font styles to use
Decorative

Colors
abd036
aaaaaa
5c5c5c

Requirements
Should not have
• Pics of dead insects, prefer nature inspired designs, frogs, trees etc
• Have attached old log & business name ( now my ex's business) Bug Begone Bay -

```html
<!DOCTYPE html>
<html lang="en">
<head>
<meta charset="utf-8">
<title>Bug Begone Bay – Business Card</title>
<link rel="stylesheet" href="https://fonts.googleapis.com/css2?family=Tinos&family=Questrial&display=swap">
<style>
  :root {
    --stage: #e4e5e4;
    --card-white: #ffffff;
    --ink-green: #2a6b33;
    --logo-box: #f1f2f1;
    --back-green-light: #2f7a4c;
    --back-green-dark: #1b5e35;
    --reverse-text: #ffffff;
  }
  * { box-sizing: border-box; margin: 0; padding: 0; }
  html, body { width: 1200px; height: 1200px; overflow: hidden; }
  body {
    background: var(--stage);
    position: relative;
    font-family: "Questrial", "Century Gothic", sans-serif;
  }
  .card {
    position: absolute;
    left: 180px;
    width: 840px;
    height: 480px;
    border-radius: 26px;
    box-shadow: 0 10px 30px rgba(0,0,0,0.15);
    overflow: hidden;
  }
  .card--front { top: 90px; background: var(--card-white); }
  .card--back {
    top: 630px;
    background: linear-gradient(135deg, var(--back-green-dark), var(--back-green-light) 55%, var(--back-green-dark));
    display: flex;
    align-items: center;
    justify-content: center;
  }

  .brand-panel {
    position: absolute;
    left: 70px; top: 120px;
    width: 330px; height: 200px;
    background: var(--logo-box);
    display: flex;
    align-items: center;
    justify-content: center;
    gap: 14px;
  }
  .brand-name {
    font-family: "Tinos", "Times New Roman", serif;
    color: var(--ink-green);
    font-size: 32px;
    line-height: 1.15;
    white-space: nowrap;
  }
  .brand-dot {
    width: 22px; height: 22px;
    border-radius: 50%;
    background: var(--ink-green);
    flex: none;
  }

  .divider {
    position: absolute;
    left: 445px; top: 85px;
    width: 3px; height: 310px;
    background: var(--ink-green);
  }

  .contact {
    position: absolute;
    left: 485px; top: 105px;
    right: 30px;
    color: var(--ink-green);
  }
  .contact__name { font-size: 34px; font-weight: 700; letter-spacing: 0.3px; white-space: nowrap; }
  .contact__title { font-size: 24px; margin-top: 2px; margin-bottom: 16px; }
  .contact__row {
    display: flex; align-items: center; gap: 14px;
    font-size: 22px; line-height: 34px;
  }
  .contact__row svg { width: 20px; height: 20px; flex: none; }
  .contact__address { font-size: 22px; line-height: 28px; margin-top: 10px; }

  .back-brand { display: flex; align-items: center; gap: 18px; }
  .back-brand .brand-name { color: var(--reverse-text); font-size: 44px; }
  .back-brand .brand-dot { background: var(--reverse-text); width: 28px; height: 28px; }
</style>
</head>
<body>

  <section class="card card--front">
    <div class="brand-panel">
      <span class="brand-dot"></span>
      <span class="brand-name">Bug Begone Bay</span>
    </div>

    <div class="divider"></div>

    <div class="contact">
      <p class="contact__name">Corinne Waldrake</p>
      <p class="contact__title">Your Title</p>
      <p class="contact__row">
        <svg viewBox="0 0 24 24" aria-hidden="true"><path fill="#2a6b33" d="M6.6 10.8a15 15 0 0 0 6.6 6.6l2.2-2.2c.3-.3.7-.4 1-.2 1.1.4 2.3.6 3.6.6.6 0 1 .4 1 1V20c0 .6-.4 1-1 1A17 17 0 0 1 3 4c0-.6.4-1 1-1h3.5c.6 0 1 .4 1 1 0 1.3.2 2.5.6 3.6.1.3 0 .7-.2 1z"/></svg>
        0428316952
      </p>
      <p class="contact__row">
        <svg viewBox="0 0 24 24" aria-hidden="true"><rect x="2" y="5" width="20" height="14" rx="2" fill="#2a6b33"/><path d="M3 6l9 7 9-7" stroke="#fff" stroke-width="1.6" fill="none"/></svg>
        youremail@gmail.com
      </p>
      <p class="contact__row">
        <svg viewBox="0 0 24 24" aria-hidden="true"><circle cx="12" cy="12" r="10" fill="#2a6b33"/><path d="M2 12h20M12 2c3 3 3 17 0 20M12 2c-3 3-3 17 0 20" stroke="#fff" stroke-width="1.3" fill="none"/></svg>
        www.yourwebsite.com
      </p>
      <p class="contact__address">Your address, city<br>state, ZIP 0000</p>
    </div>
  </section>

  <section class="card card--back">
    <div class="back-brand">
      <span class="brand-dot"></span>
      <span class="brand-name">Bug Begone Bay</span>
    </div>
  </section>

</body>
</html>
```